Courier Business needs a Business Card Design !!!

My new company needs a business card design. Our company name is Maple Dart Courier & Delivery Services. We will be servicing residential , government and business clients in the City of Yellowknife, Northwest Territories, Canada. I would like the following information included on the card: Name- Calvin Oxley. Title- Owner. Company- Maple Dart Courier & Delivery Services. Address- PO Box 5918 , Yellowknife , NWT, X0E 4K3. Phone- 867-555-0193. Email- mapledartdelivery@postfern.example. Facebook- www.socialpage.example/mapledartdelivery. I would like my double sided card to be the standard size of 84mm x 55mm. No borders. Use CMYK mode.1039x 697 pixels at least. I would like my logo to take up at least one quarter of the area of one side of the card. Text should be at least 8 point with perhaps my name being 10 point and my company name being 12-15 point . It should have clear readable font. Please use one or two bold colors. I am trying to attract the business community so a professional look might be best. My tag line is " On Time Every Time ". Nice safe margins please. We will be providing fast, reliable and professional delivery of envelopes and small packages within the City of Yellowknife. We offer 100% satisfaction or a complete refund. I have included a file of our logo. I like black, blue and red but am willing to look at what you feel would work best. I do not really like white as a background color.

Target Market(s)

Professionals , business owners. 30-50 years old

Industry/Entity Type

Residential

Contact Information for Business Card

As noted in brief

Font styles to use
Serif
Sans Serif

Colors
000000
0255a3
f04a50

Requirements
Must have
• My contact info. My logo
Nice to have
• Simple elegant design but still catches the eye
Should not have
• White background color

```html
<!DOCTYPE html>
<html lang="en">
<head>
<meta charset="utf-8">
<title>Maple Dart Courier &amp; Delivery Services – Business Card</title>
<link rel="stylesheet" href="https://fonts.googleapis.com/css2?family=Arimo:wght@400;700&family=Gochi+Hand&display=swap">
<style>
  :root {
    --brand-blue: #3853a4;
    --paper-tint: #e4e9f5;
    --ink-light: #ffffff;
  }
  * { margin: 0; padding: 0; box-sizing: border-box; }
  html, body {
    width: 1200px;
    height: 792px;
    overflow: hidden;
    background: var(--paper-tint);
  }
  .card {
    position: relative;
    width: 1200px;
    height: 792px;
    background: var(--paper-tint);
    font-family: "Arimo", Arial, sans-serif;
    overflow: hidden;
  }
  .card__wave {
    position: absolute;
    inset: 0;
    width: 1200px;
    height: 792px;
  }
  .card__wave path { fill: var(--brand-blue); }
  .card__line {
    position: absolute;
    left: 0;
    width: 100%;
    text-align: center;
    white-space: nowrap;
  }
  .brand {
    top: 52px;
    display: flex;
    justify-content: center;
    align-items: center;
    gap: 18px;
    font-size: 46px;
    color: var(--ink-light);
  }
  .brand__mark {
    width: 34px;
    height: 34px;
    border-radius: 50%;
    background: var(--ink-light);
    flex: none;
  }
  .owner {
    top: 128px;
    font-size: 36px;
    font-weight: 700;
    color: var(--ink-light);
  }
  .owner__title { font-weight: 400; }
  .company-phone {
    top: 188px;
    font-size: 44px;
    color: var(--ink-light);
  }
  .tagline {
    top: 296px;
    font-family: "Gochi Hand", cursive;
    font-size: 72px;
    color: var(--ink-light);
    letter-spacing: 1px;
  }
  .social-page {
    top: 556px;
    font-size: 50px;
    font-weight: 700;
    color: var(--brand-blue);
    letter-spacing: 0.5px;
  }
  .contact-email,
  .contact-address {
    font-size: 39px;
    color: var(--brand-blue);
  }
  .contact-email { top: 650px; }
  .contact-address { top: 703px; }
</style>
</head>
<body>
  <main class="card">
    <svg class="card__wave" viewBox="0 0 1200 792" aria-hidden="true">
      <path d="M0,0 H1200 V514 C970,521 606,497 364,436 C194,388 73,315 0,255 Z"/>
    </svg>

    <p class="card__line brand"><span class="brand__mark" aria-hidden="true"></span><span class="brand__name">Maple Dart Courier &amp; Delivery Services</span></p>
    <p class="card__line owner">Calvin Oxley <span class="owner__title">– Owner</span></p>
    <p class="card__line company-phone">Phone- 867-555-0193</p>
    <p class="card__line tagline">ON TIME EVERY TIME!</p>

    <p class="card__line social-page">socialpage.example/mapledartdelivery</p>
    <p class="card__line contact-email">Email:&nbsp; mapledartdelivery@postfern.example</p>
    <p class="card__line contact-address">Address: PO Box 5918 , Yellowknife , NWT, X0E 4K3</p>
  </main>
</body>
</html>
```